Blue Harbor Trophies & Awards Unique Business Card Design

Recently selected a new logo design and waiting to recieve print files. I've attached image for your review. We are a trophies and awards company that provides engraving on trophies, plaques, name plates, name tags, desk sets, medals, acrylics, and signage.

We are located in Monroe, Louisiana and provide this service with computerized & laser engraving equipment.

Target Market(s)

Corporate, Sport, Church, and Special Events

Industry/Entity Type

Business

Contact Information for Business Card

I'd like to see the following list on the card: Trophies, Plaques, Name Plates, Name Tags, Desk Sets, Medals, Certificates... this is accomplished with Computerized & Laser Engraving

Colors
0555a3
ec1f27
ffffff

Requirements
Must have
• I like either single or double sided. If a design can be created with a frosted card stock I'd consider single. Must be Red, White, and Blue. Dale Penrow - Owner, 415 W 9th Ave, Monroe, La 70384 office 318-555-2190 fax 318-555-2186 email: blueharbor@blueharbortrophyco.example, and website: www.blueharbortrophyco.example

```html
<!DOCTYPE html>
<html lang="en">
<head>
<meta charset="utf-8">
<title>Blue Harbor Trophies &amp; Awards – Business Card</title>
<link rel="stylesheet" href="https://fonts.googleapis.com/css2?family=Arimo:wght@400;700&family=Italianno&display=swap">
<style>
  :root {
    --page-bg: #d8d2c9;
    --card-top: #f4f5f7;
    --card-bottom: #e3e4e8;
    --brand-blue: #0555a3;
    --brand-red: #c8262d;
    --ink-navy: #26336e;
    --ink-muted: #4b5784;
  }
  html, body {
    margin: 0;
    width: 1200px;
    height: 970px;
    overflow: hidden;
    background: var(--page-bg);
  }
  .card {
    position: absolute;
    left: 50px;
    top: 179px;
    width: 1100px;
    height: 612px;
    background: linear-gradient(160deg, var(--card-top) 0%, #eceef2 55%, var(--card-bottom) 100%);
    border: 1px solid #c9c9cc;
    box-shadow: 0 10px 30px rgba(0,0,0,0.18);
    font-family: "Arimo", Arial, sans-serif;
  }
  .brand-name {
    position: absolute;
    left: 0;
    right: 0;
    top: 112px;
    margin: 0;
    text-align: center;
    font-size: 54px;
    font-weight: 700;
    color: var(--brand-blue);
    letter-spacing: 0.5px;
  }
  .person-name {
    position: absolute;
    left: 48px;
    top: 250px;
    margin: 0;
    font-family: "Italianno", cursive;
    font-weight: 400;
    font-size: 66px;
    line-height: 1;
    color: var(--brand-red);
  }
  .person-title {
    position: absolute;
    left: 48px;
    top: 342px;
    margin: 0;
    font-size: 23px;
    color: var(--ink-muted);
  }
  .contact-list {
    position: absolute;
    left: 48px;
    top: 405px;
    margin: 0;
    padding: 0;
    list-style: none;
    font-size: 26px;
    color: var(--ink-muted);
  }
  .contact-list li {
    display: flex;
    align-items: flex-start;
    line-height: 36px;
  }
  .contact-icon {
    width: 28px;
    height: 28px;
    margin: 4px 22px 0 0;
    flex: none;
    fill: var(--ink-navy);
  }
  .services-heading {
    position: absolute;
    left: 700px;
    top: 290px;
    margin: 0;
    font-family: "Italianno", cursive;
    font-weight: 400;
    font-size: 50px;
    color: var(--brand-red);
  }
  .services-list {
    position: absolute;
    left: 705px;
    top: 354px;
    margin: 0;
    padding: 0;
    list-style: none;
    font-size: 28px;
    line-height: 32px;
    color: var(--ink-navy);
  }
  .services-list li::before {
    content: "\25C6";
    display: inline-block;
    width: 34px;
    font-size: 20px;
    color: var(--ink-navy);
  }
</style>
</head>
<body>
  <div class="card">
    <h1 class="brand-name">Blue Harbor Trophies &amp; Awards</h1>

    <h2 class="person-name">Dale Penrow</h2>
    <p class="person-title">Owner</p>

    <ul class="contact-list">
      <li>
        <svg class="contact-icon" viewBox="0 0 24 24" aria-hidden="true"><path d="M6.6 10.8a15.1 15.1 0 0 0 6.6 6.6l2.2-2.2c.3-.3.7-.4 1-.2 1.1.4 2.3.6 3.6.6.6 0 1 .4 1 1V20c0 .6-.4 1-1 1A17 17 0 0 1 3 4c0-.6.4-1 1-1h3.5c.6 0 1 .4 1 1 0 1.3.2 2.5.6 3.6.1.3 0 .7-.2 1z"/></svg>
        <span>318-555-2190</span>
      </li>
      <li>
        <svg class="contact-icon" viewBox="0 0 24 24" aria-hidden="true"><path d="M3 6h18v12H3z M3 6l9 7 9-7" fill="none" stroke="#26336e" stroke-width="2"/></svg>
        <span>blueharbor@blueharbortrophyco.example</span>
      </li>
      <li>
        <svg class="contact-icon" viewBox="0 0 24 24" aria-hidden="true"><circle cx="12" cy="12" r="10"/><path d="M7 7c2 0 3 1 3 3s-2 2-2 4 2 2 2 4M15 5c-1 2 1 3 3 3M14 14c1 1 3 1 4 3" fill="none" stroke="#eceef2" stroke-width="1.6"/></svg>
        <span>www.blueharbortrophyco.example</span>
      </li>
      <li>
        <svg class="contact-icon" viewBox="0 0 24 24" aria-hidden="true"><path d="M12 2a7 7 0 0 0-7 7c0 5 7 13 7 13s7-8 7-13a7 7 0 0 0-7-7zm0 9.5A2.5 2.5 0 1 1 12 6.5a2.5 2.5 0 0 1 0 5z"/></svg>
        <span>415 W 9th Ave<br>Monroe, LA&nbsp; 70384</span>
      </li>
    </ul>

    <h3 class="services-heading">Services</h3>
    <ul class="services-list">
      <li>engraving on trophies</li>
      <li>plaques</li>
      <li>name plates</li>
      <li>name tags</li>
      <li>desk sets</li>
      <li>medals</li>
      <li>acrylics, and signage</li>
    </ul>
  </div>
</body>
</html>
```